Business Cards

I'd like help creating business cards with the full logo "Veltrona Capital Partners" on the back of the card (navy background with white writing), and abbreviated logo "VCP" on the front. Would like to list name, title, phone number, email, and website listed on front of card. Would like to keep very simple. Front font Arial or similar.

```html
<!DOCTYPE html>
<html lang="en">
<head>
<meta charset="utf-8">
<title>Veltrona Capital Partners — Business Cards</title>
<link rel="stylesheet" href="https://fonts.googleapis.com/css2?family=Ubuntu:wght@400;500;700&display=swap">
<style>
  :root {
    --navy: #1f3566;
    --white: #ffffff;
    --ink: #000000;
    --page: #ffffff;
    --card-shadow: rgba(0, 0, 0, 0.28);
  }
  * { margin: 0; padding: 0; box-sizing: border-box; }
  html, body {
    width: 1200px; height: 1200px; overflow: hidden;
    background: var(--page);
    font-family: "Ubuntu", Arial, sans-serif;
  }
  .card {
    position: absolute;
    left: 165px;
    width: 870px; height: 509px;
    box-shadow: 0 1px 4px var(--card-shadow);
    overflow: hidden;
  }
  .card--front { top: 66px; background: var(--white); }
  .card--back { top: 626px; background: var(--navy); }

  .front-panel {
    position: absolute; inset: 0;
    width: 870px; height: 509px;
    filter: drop-shadow(-6px 8px 7px rgba(0,0,0,0.35));
  }
  .front-panel polygon { fill: var(--navy); }

  .short-name {
    position: absolute;
    left: 207px; top: 252px;
    transform: translate(-50%, -50%);
    font-weight: 500; font-size: 96px; letter-spacing: 2px;
    color: var(--ink);
  }

  .identity {
    position: absolute; right: 65px; top: 190px;
    text-align: right; color: var(--white);
  }
  .identity__name { font-weight: 700; font-size: 32px; line-height: 1.1; }
  .identity__title { font-weight: 400; font-size: 20px; margin-top: 4px; }

  .contact {
    position: absolute; right: 55px; top: 340px;
    list-style: none; color: var(--white);
    font-size: 20px; font-weight: 400;
  }
  .contact__item {
    display: flex; align-items: center; justify-content: flex-end;
    height: 33.5px;
  }
  .contact__icon { width: 14px; height: 14px; margin-left: 22px; fill: var(--white); }

  .brand {
    position: absolute; left: 50%; top: 275px;
    transform: translate(-50%, -50%);
    text-align: center; color: var(--white); font-weight: 500;
    white-space: nowrap;
  }
  .brand__name { font-size: 84px; letter-spacing: 5px; line-height: 1; }
  .brand__sub { font-size: 28px; letter-spacing: 9px; margin-top: 18px; }
</style>
</head>
<body>
  <section class="card card--front" aria-label="Business card front">
    <svg class="front-panel" viewBox="0 0 870 509" aria-hidden="true">
      <polygon points="347,0 870,0 870,509 454,509 454,384 400,384 400,128 347,128"/>
    </svg>
    <div class="short-name">VCP</div>
    <div class="identity">
      <div class="identity__name">Dorian K Halvers III</div>
      <div class="identity__title">Attorney at Law</div>
    </div>
    <ul class="contact">
      <li class="contact__item">800-555-0142
        <svg class="contact__icon" viewBox="0 0 16 16" aria-hidden="true"><path d="M3.6 1l2.3 3-1.3 1.6c.9 2 2.6 3.8 4.8 4.8L11 9.1l3 2.3-1.2 2.6C7 14 2 9 2 2.2z"/></svg>
      </li>
      <li class="contact__item">422-555-0187
        <svg class="contact__icon" viewBox="0 0 16 16" aria-hidden="true"><path d="M4 1h8v4H4zM1 6h14v6h-3v3H4v-3H1zm4 4v4h6v-4z"/></svg>
      </li>
      <li class="contact__item">info@vcp.com
        <svg class="contact__icon" viewBox="0 0 16 16" aria-hidden="true"><path d="M1 3h14v1.2L8 9 1 4.2zM1 6l7 4.8L15 6v7H1z"/></svg>
      </li>
      <li class="contact__item">VCP.com
        <svg class="contact__icon" viewBox="0 0 16 16" aria-hidden="true"><circle cx="8" cy="8" r="6.5" fill="none" stroke="#fff" stroke-width="1.4"/><path d="M1.5 8h13M8 1.5c-3 3.5-3 9.5 0 13M8 1.5c3 3.5 3 9.5 0 13" fill="none" stroke="#fff" stroke-width="1.2"/></svg>
      </li>
    </ul>
  </section>

  <section class="card card--back" aria-label="Business card back">
    <div class="brand">
      <div class="brand__name">VELTRONA</div>
      <div class="brand__sub">CAPITAL PARTNERS</div>
    </div>
  </section>
</body>
</html>
```